Capital Management company needs a web design

We have a domain name and logo but need hosting and design. Please look at the Must-Haves section.

Target Market(s)

banking industry and investors

Industry/Entity Type

Investment

Coding

Coded - Design and coding required

Number of Pages Required

1 page

Font styles to use
Sans Serif

Requirements
Must have
• Picture(s) of skyscraper skyline (can be of Manhattan, Chicago, or any other major city in the USA).
• Please use the three colors of the logo as a backdrop to part of the webpage(s)
Should not have
• No "what our clients say" section
• No pictures of people

```html
<!DOCTYPE html>
<html lang="en">
<head>
<meta charset="utf-8">
<title>Harbor Crest Management</title>
<link href="https://fonts.googleapis.com/css2?family=Open+Sans:wght@400;600;700&display=swap" rel="stylesheet">
<style>
:root{
  --red:#e0262b;
  --blue:#1a7ff5;
  --green:#28a745;
  --band:#f3f3f3;
  --ink:#222;
  --muted:#555;
  --white:#fff;
}
*{box-sizing:border-box;margin:0;padding:0}
html,body{width:1200px;height:3456px;overflow:hidden}
body{font-family:"Open Sans",sans-serif;color:var(--ink);background:var(--white);font-size:15px;line-height:1.5}
a{color:inherit;text-decoration:none}
.brand{display:flex;align-items:center;gap:10px}
.brand-mark{width:26px;height:26px;background:var(--blue);border-radius:4px}
.brand-name{font-weight:700;font-size:17px;color:var(--blue);line-height:1.1;width:150px}

.site-header{height:68px;display:flex;align-items:center;justify-content:space-between;padding:0 24px}
.nav{display:flex;align-items:center;gap:18px;font-size:15px}
.btn-outline{border:1.5px solid;border-radius:4px;padding:4px 12px;font-size:14px}
.btn-signin{color:var(--green);border-color:var(--green)}
.btn-signup{color:var(--blue);border-color:var(--blue)}

.hero{position:relative;height:684px}
.hero-photo{position:absolute;inset:0;background:radial-gradient(ellipse at 30% 10%,#8c8f96 0%,#3a3f4a 35%,#1b1e25 70%),linear-gradient(#555,#111)}
.hero-title{position:absolute;left:176px;top:300px;color:var(--white);font-size:44px;font-weight:400;line-height:1.35}
.hero-title .accent{background:var(--red);padding:0 10px}

.features{height:224px;display:grid;grid-template-columns:repeat(4,1fr);padding:30px 40px 0;text-align:center}
.feature-icon{width:44px;height:44px;border-radius:50%;background:var(--red);margin:0 auto 8px;display:flex;align-items:center;justify-content:center}
.feature h3{font-size:19px;font-weight:600}
.feature p{font-size:14px;color:var(--muted);max-width:220px;margin:0 auto}

.overview{height:224px;background:var(--band);text-align:center;padding-top:20px}
.section-title{font-size:40px;font-weight:600;line-height:1.3}
.section-lead{font-size:14px;color:var(--muted);max-width:760px;margin:6px auto 0;line-height:1.45}
.btn-red{display:inline-block;margin-top:12px;background:var(--red);color:var(--white);font-size:14px;padding:6px 16px;border-radius:3px}

.posts{height:832px;text-align:center;padding-top:16px}
.post-grid{display:grid;grid-template-columns:392px 388px 380px;gap:12px 16px;margin-top:28px;text-align:left}
.post-photo{height:280px;background:linear-gradient(135deg,#b9b9b6,#6f6a66 60%,#3c3a38)}
.post-photo.b{background:linear-gradient(135deg,#d6d2cc,#8d8177 55%,#4e4640)}
.post-photo.c{background:linear-gradient(135deg,#e8ecef,#a9b4bd 55%,#6d7880)}
.post h3{font-size:31px;font-weight:600;line-height:1.2;margin:12px 0 16px}
.post p{font-size:15px;color:var(--muted);line-height:1.6}
.read-more{display:block;color:var(--red);font-size:14px;margin-top:36px}

.slider{position:relative;height:496px}
.slider-photo{position:absolute;inset:0;background:linear-gradient(120deg,#3a3a3c,#1f2125 50%,#4a4c50)}
.arrow{position:absolute;top:234px}
.arrow.left{left:26px}.arrow.right{right:26px}
.dots{position:absolute;top:408px;left:0;right:0;display:flex;justify-content:center;gap:8px}
.dots span{width:24px;height:24px;border-radius:50%;background:#9a9a9a}
.dots span.on{background:var(--white)}

.services{height:580px;background:var(--blue);color:var(--white);text-align:center;padding-top:22px}
.services .section-lead{color:#e8f1ff}
.service-grid{display:grid;grid-template-columns:344px 344px 376px;gap:24px;justify-content:center;margin-top:30px}
.service{border:1.5px solid rgba(255,255,255,.8);height:192px;padding-top:28px}
.service-icon{width:18px;height:18px;border-radius:50%;background:var(--white);margin:0 auto 4px}
.service h4{font-size:16px;font-weight:600}
.service p{font-size:14px;max-width:230px;margin:4px auto 0}

.site-footer{height:292px;display:grid;grid-template-columns:560px 300px 1fr;padding:20px 28px 0}
.footer-about p{font-size:14px;color:var(--muted);margin-top:12px;line-height:1.45}
.footer-about .read-more{color:var(--blue);margin-top:40px}
.footer-col h5{font-size:22px;font-weight:600;line-height:1.2}
.footer-col ul{list-style:disc;padding-left:44px;margin-top:8px;font-size:14px;color:var(--blue);line-height:1.7}
.contact{display:flex;gap:12px;margin-top:8px}
.contact ul{list-style:disc;padding-left:20px;margin:0;font-size:14px;color:var(--blue);line-height:1.7}
.contact-info{font-size:14px;color:var(--muted);line-height:1.5}
.contact-info div{margin-bottom:14px}

.copyright{height:56px;background:#f7f7f7;display:flex;align-items:center;justify-content:space-between;padding:0 28px;font-size:14px;color:var(--muted)}
.social{display:flex;gap:18px}
.social span{width:16px;height:16px;background:#333;border-radius:3px}
</style>
</head>
<body>

<header class="site-header">
  <div class="brand"><span class="brand-mark"></span><span class="brand-name">Harbor Crest Management</span></div>
  <nav class="nav">
    <a href="#">Home</a><a href="#">About us</a><a href="#">Invest</a><a href="#">services</a><a href="#">FAQs</a>
    <a class="btn-outline btn-signin" href="#">Sign in</a>
    <a class="btn-outline btn-signup" href="#">Sign up</a>
  </nav>
</header>

<section class="hero">
  <div class="hero-photo" role="img" aria-label="Night skyline of city skyscrapers"></div>
  <h1 class="hero-title">We're an Independent<br>management <span class="accent">Company</span></h1>
</section>

<section class="features">
  <div class="feature"><div class="feature-icon"><svg width="20" height="20" viewBox="0 0 20 20"><circle cx="10" cy="8" r="5" fill="none" stroke="#fff" stroke-width="2"/><rect x="8" y="14" width="4" height="3" fill="#fff"/></svg></div><h3>Great Ideas</h3><p>Lorem ipsum dolor sit amet, consectetur adipisicing elit. Nemo culpa!</p></div>
  <div class="feature"><div class="feature-icon"><svg width="20" height="20" viewBox="0 0 20 20"><circle cx="10" cy="10" r="6" fill="none" stroke="#fff" stroke-width="3" stroke-dasharray="3 2"/></svg></div><h3>Quick Settings</h3><p>Lorem ipsum dolor sit amet, consectetur adipisicing elit. Nemo culpa!</p></div>
  <div class="feature"><div class="feature-icon"><svg width="20" height="20" viewBox="0 0 20 20"><rect x="3" y="7" width="14" height="10" rx="1" fill="#fff"/><rect x="7" y="4" width="6" height="4" fill="none" stroke="#fff" stroke-width="2"/></svg></div><h3>Invest</h3><p>Lorem ipsum dolor sit amet, consectetur adipisicing elit. Nemo culpa!</p></div>
  <div class="feature"><div class="feature-icon"><svg width="20" height="20" viewBox="0 0 20 20"><path d="M10 17 3 10a4 4 0 0 1 7-5 4 4 0 0 1 7 5z" fill="#fff"/></svg></div><h3>Saving</h3><p>Lorem ipsum dolor sit amet, consectetur adipisicing elit. Nemo culpa!</p></div>
</section>

<section class="overview">
  <h2 class="section-title">Company Overview</h2>
  <p class="section-lead">Lorem ipsum dolor sit amet consectetur adipisicing elit. Quibusdam laboriosam eum, minus aliquam, suscipit totam aspernatur labore vero maxime quas ipsam aperiam ea cillum. Eaque voluptate porro numquam illo laborum.</p>
  <a class="btn-red" href="#">View More</a>
</section>

<section class="posts">
  <h2 class="section-title">Latest Post</h2>
  <p class="section-lead">Lorem ipsum dolor sit amet consectetur adipisicing elit. Quibusdam laboriosam eum, minus aliquam, suscipit totam aspernatur labore vero maxime quas ipsam aperiam ea cillum. Eaque voluptate porro numquam illo laborum.</p>
  <div class="post-grid">
    <article class="post"><div class="post-photo" role="img" aria-label="Laptop on an office desk"></div><h3>Lorem ipsum dolor sit amet, consectetur adipisicing elit.</h3><p>Lorem ipsum dolor sit amet, consectetur adipisicing elit. Hic, dolorem rerum exercitationem, autem nemo cupiditate dignissimos dolores aperiam rem perferendis cumque sit voluptate asperiores excepturi laborum officia ut nobis repellat.</p><a class="read-more" href="#">Read More</a></article>
    <article class="post"><div class="post-photo b" role="img" aria-label="Business paperwork on a table"></div><h3>Lorem ipsum dolor sit amet, consectetur adipisicing elit.</h3><p>Lorem ipsum dolor sit amet, consectetur adipisicing elit. Hic, dolorem rerum exercitationem, autem nemo cupiditate dignissimos dolores aperiam rem perferendis cumque sit voluptate asperiores excepturi laborum officia ut nobis repellat.</p><a class="read-more" href="#">Read More</a></article>
    <article class="post"><div class="post-photo c" role="img" aria-label="Bright workspace with keyboard"></div><h3>Lorem ipsum dolor sit amet, consectetur adipisicing elit.</h3><p>Lorem ipsum dolor sit amet, consectetur adipisicing elit. Hic, dolorem rerum exercitationem, autem nemo cupiditate dignissimos dolores aperiam rem perferendis cumque sit voluptate asperiores excepturi laborum officia ut nobis repellat.</p><a class="read-more" href="#">Read More</a></article>
  </div>
</section>

<section class="slider">
  <div class="slider-photo" role="img" aria-label="Dark modern office workspace"></div>
  <svg class="arrow left" width="16" height="28" viewBox="0 0 16 28"><path d="M13 3 3 14l10 11" fill="none" stroke="#fff" stroke-width="3"/></svg>
  <svg class="arrow right" width="16" height="28" viewBox="0 0 16 28"><path d="M3 3l10 11L3 25" fill="none" stroke="#fff" stroke-width="3"/></svg>
  <div class="dots"><span></span><span class="on"></span><span></span></div>
</section>

<section class="services">
  <h2 class="section-title">Our best services</h2>
  <p class="section-lead">Lorem ipsum dolor sit amet, consectetur adipisicing elit. Nihil, praesentium, facilis. Obcaecati aliquam voluptatum neque, reprehenderit quo, quidem ab nam!</p>
  <div class="service-grid">
    <div class="service"><div class="service-icon"></div><h4>Ecommerce solution</h4><p>Lorem ipsum dolor sit amet, consectetur adipisicing elit. Pariatur, magnam!</p></div>
    <div class="service"><div class="service-icon"></div><h4>Buisness Financing</h4><p>Lorem ipsum dolor sit amet, consectetur adipisicing elit. Pariatur, magnam!</p></div>
    <div class="service"><div class="service-icon"></div><h4>Product Marketing</h4><p>Lorem ipsum dolor sit amet, consectetur adipisicing elit. Pariatur, magnam!</p></div>
    <div class="service"><div class="service-icon"></div><h4>Business data</h4><p>Lorem ipsum dolor sit amet, consectetur adipisicing elit. Pariatur, magnam!</p></div>
    <div class="service"><div class="service-icon"></div><h4>Custom work</h4><p>Lorem ipsum dolor sit amet, consectetur adipisicing elit. Pariatur, magnam!</p></div>
    <div class="service"><div class="service-icon"></div><h4>Investment</h4><p>Lorem ipsum dolor sit amet, consectetur adipisicing elit. Pariatur, magnam!</p></div>
  </div>
</section>

<footer class="site-footer">
  <div class="footer-about">
    <div class="brand"><span class="brand-mark"></span><span class="brand-name">Harbor Crest Management</span></div>
    <p>Lorem ipsum dolor sit amet, consectetur adipisicing elit. Maxime accusamus mollitia dolor enim vel velit, animi, assumenda perferendis fugit quos corporis architecto distinctio recusandae esse voluptatem dolore magnam. Modi omnis aliquam doloribus natus, necessitatibus rerum, quos repellat.</p>
    <a class="read-more" href="#">Read More</a>
  </div>
  <div class="footer-col">
    <h5>Helpful links</h5>
    <ul><li>About</li><li>About</li><li>About</li><li>About</li><li>About</li></ul>
  </div>
  <div class="footer-col">
    <h5>Contact Us</h5>
    <div class="contact">
      <ul><li>About</li><li>About</li><li>About</li><li>About</li><li>About</li></ul>
      <div class="contact-info">
        <div>4120 Alder Lane Near Birch Fork, US</div>
        <div>Phone: 000-55501234</div>
        <div>Email: info@harborcrest.com</div>
      </div>
    </div>
  </div>
</footer>

<div class="copyright">
  <span>COPYRIGHT 2018 Harbor Crest Management | ALL RIGHTS RESERVED</span>
  <div class="social"><span></span><span></span><span></span><span></span><span></span></div>
</div>

</body>
</html>
```